M25 Billboard Advert Required Please

I need an advert for a motorway Billboard on the M25 , the advert should show the following in big letters:
GUTTER CLEANING
TOMSDRAINWORKS.NET and a small logo off to the side (Our logo is attached)

The printer has requested the following (Important please) the advert has to be
pdf file / 300 dpi/landscape orientation / scaled to a minimum 25% advert size ( this particular site is 22ft x 10ft so 25% of this please). Please also make sure that the artwork is embedded and outlined correctly if this is incorrect it will affect the printing of the banner.
Updates

Need extra days to review

Target Market(s)

General Public

Industry/Entity Type

Gutter Cleaning

Requirements
Should not have
• No Change to our Logo

```html
<!DOCTYPE html>
<html lang="en">
<head>
<meta charset="utf-8">
<title>Gutter Cleaning – Billboard</title>
<link rel="stylesheet" href="https://fonts.googleapis.com/css2?family=Montserrat:ital,wght@0,700;1,700;1,800;1,900&family=Open+Sans:wght@600&display=swap">
<style>
  :root {
    --page-bg: #9d9d9d;
    --board-light: #f1f1f3;
    --board-shade: #e4e5e8;
    --brand-red: #b91f2a;
    --ink: #0a0a0a;
    --white: #ffffff;
    --tagline: #2a2a2a;
  }
  html, body {
    margin: 0;
    padding: 0;
    width: 887px;
    height: 1200px;
    overflow: hidden;
    background: var(--page-bg);
  }
  .billboard {
    position: absolute;
    left: 18px;
    top: 406px;
    width: 851px;
    height: 387px;
    box-shadow: 0 2px 6px rgba(0,0,0,0.25);
  }
  .billboard svg { display: block; width: 100%; height: 100%; }
  .headline-top {
    font-family: "Montserrat", sans-serif;
    font-style: italic;
    font-weight: 800;
    fill: var(--brand-red);
  }
  .headline-bottom {
    font-family: "Montserrat", sans-serif;
    font-style: italic;
    font-weight: 900;
    fill: var(--ink);
  }
  .web-address {
    font-family: "Montserrat", sans-serif;
    font-style: italic;
    font-weight: 800;
    fill: var(--white);
  }
  .brand-name {
    font-family: "Montserrat", sans-serif;
    font-weight: 700;
    fill: var(--ink);
  }
  .brand-tagline {
    font-family: "Open Sans", sans-serif;
    font-weight: 600;
    fill: var(--tagline);
  }
  .brand-square { fill: var(--brand-red); }
  .accent-block, .address-band { fill: var(--brand-red); }
</style>
</head>
<body>
  <div class="billboard">
    <svg viewBox="0 0 851 387" xmlns="http://www.w3.org/2000/svg">
      <defs>
        <linearGradient id="boardGradient" x1="0" y1="0" x2="1" y2="1">
          <stop offset="0" stop-color="var(--board-light)"/>
          <stop offset="0.5" stop-color="var(--board-shade)"/>
          <stop offset="1" stop-color="var(--board-light)"/>
        </linearGradient>
      </defs>
      <rect class="board-surface" width="851" height="387" fill="url(#boardGradient)"/>

      <polygon class="accent-block" points="705,26 851,26 851,126 692,126"/>

      <text class="headline-top" x="34" y="126" font-size="140" textLength="636" lengthAdjust="spacingAndGlyphs">GUTTER</text>
      <text class="headline-bottom" x="34" y="259" font-size="148" textLength="790" lengthAdjust="spacingAndGlyphs">CLEANING</text>

      <polygon class="address-band" points="0,295 569,295 557,361 0,361"/>
      <text class="web-address" x="29" y="340" font-size="30" textLength="505" lengthAdjust="spacingAndGlyphs">WWW.TOMSDRAINWORKS.NET</text>

      <rect class="brand-square" x="602" y="297" width="22" height="22"/>
      <text class="brand-name" x="632" y="317" font-size="24" textLength="193" lengthAdjust="spacingAndGlyphs">Tom's Drainworks</text>
      <text class="brand-tagline" x="600" y="357" font-size="12.5" textLength="225" lengthAdjust="spacingAndGlyphs">Clean gutters protect your property</text>
    </svg>
  </div>
</body>
</html>
```